Book cover required for new book business book (Otter Ambush SEO for Managed Service Providers)

We are finalizing publishing dates for our latest business book. The audience this book is targetting is IT business owners. Demographic age 30-50 years of age, male, middle class. The title of the book is Otter Ambush SEO for managed service providers. The author name is Dean Harrow. The book goes into details about how to improve SEO for IT businesses. The premise of the book is if a bear attacked a crowd of people, and you were in that crowd, you'd only have to be 1% faster to outrun the bear. The same is true for your IT Businesses website. You only have to put in 1% more effort into your SEO to be on page one of Zarvio.
We have been using a working draft image whilst the book has been in preproduction. I am unsure if this working image is licensed. Please find attached.

```html
<!DOCTYPE html>
<html lang="en">
<head>
<meta charset="utf-8">
<title>Otter Ambush SEO for Managed Service Providers — Book Cover</title>
<link rel="stylesheet" href="https://fonts.googleapis.com/css2?family=Montserrat:wght@700&family=Cinzel:wght@400;500&display=swap">
<style>
  :root {
    --stage-bg: #dfe6ea;
    --cover-paper: #ffffff;
    --accent-orange: #e8452c;
    --accent-orange-light: #f4603f;
    --ink-navy: #1f2a55;
    --ink-deep: #15304a;
    --tone-dark: #2a2420;
    --tone-suit: #2a2f6b;
  }
  html, body {
    margin: 0;
    padding: 0;
    width: 1200px;
    height: 1200px;
    overflow: hidden;
    background: var(--stage-bg);
  }
  .book-cover {
    position: absolute;
    left: 270px;
    top: 105px;
    width: 660px;
    height: 990px;
    background: var(--cover-paper);
    box-shadow: 0 6px 24px rgba(40, 60, 80, 0.18);
  }
  .book-cover svg {
    display: block;
    width: 100%;
    height: 100%;
  }
  .title-word {
    font-family: "Montserrat", "Helvetica Neue", Arial, sans-serif;
    font-weight: 700;
  }
  .subtitle-line {
    font-family: "Cinzel", "Times New Roman", serif;
    font-weight: 500;
    fill: var(--ink-navy);
  }
  .subtitle-accent { fill: var(--accent-orange); }
  .author-name {
    font-family: "Cinzel", "Times New Roman", serif;
    font-weight: 500;
    fill: var(--ink-deep);
  }
</style>
</head>
<body>
  <div class="book-cover">
    <svg viewBox="0 0 602 903" xmlns="http://www.w3.org/2000/svg">
      <defs>
        <linearGradient id="title-photo-tones" x1="0" y1="0" x2="1" y2="1" gradientUnits="objectBoundingBox">
          <stop offset="0" stop-color="#f4603f"/>
          <stop offset="0.22" stop-color="#e8452c"/>
          <stop offset="0.38" stop-color="#2a2f6b"/>
          <stop offset="0.52" stop-color="#2a2420"/>
          <stop offset="0.66" stop-color="#2a2f6b"/>
          <stop offset="0.82" stop-color="#e8452c"/>
          <stop offset="1" stop-color="#f4603f"/>
        </linearGradient>
      </defs>

      <g class="title-block" role="img" aria-label="Title lettering filled with a photo of a shouting businessman in a navy suit over an orange backdrop">
        <text class="title-word" x="89" y="257" font-size="171" textLength="424" lengthAdjust="spacingAndGlyphs" fill="url(#title-photo-tones)">OTTER</text>
        <text class="title-word" x="83" y="357" font-size="107" textLength="431" lengthAdjust="spacingAndGlyphs" fill="url(#title-photo-tones)">AMBUSH</text>
        <text class="title-word" x="89" y="539" font-size="233" textLength="420" lengthAdjust="spacingAndGlyphs" fill="url(#title-photo-tones)">SEO</text>
      </g>

      <text class="subtitle-line" x="146" y="591" font-size="40" textLength="305" lengthAdjust="spacingAndGlyphs"><tspan class="subtitle-accent">FOR</tspan> MANAGED</text>
      <text class="subtitle-line" x="96" y="641" font-size="40" textLength="405" lengthAdjust="spacingAndGlyphs"><tspan class="subtitle-accent">SERV</tspan>ICE PROVIDERS</text>

      <text class="author-name" x="53" y="854" font-size="46" textLength="506" lengthAdjust="spacing">DEAN HARROW</text>
    </svg>
  </div>
</body>
</html>
```